Contemporary Elegant Business Card Design for an International Trade Company in the Wine Industry

We need a new business card design for an international trade company in the wine and winemaking industry. The overall feel of the card should be contemporary, upscale, luxurious and elegant. It should communicate confidence and professionalism. The colors should complementary to our logo design (burgundy, gold, and black).
Inspiration: rich velvet tapestry
The card should include the following information:
Business: Brovenna Trading/Shipping, LLC.
Name: Marcus T. Hollenbrand
Title: CEO
Email: mark@brovennatrading.example
Phone: 555-294-6172
www.brovennatrading.example
Updates
Project Deadline Extended
Reason: We'd like the designers that we requested some additional designs from to still submit designs. Thank you!
Industry/Entity Type
Business
Contact Information for Business Card
Title: CEO
Phone: 555-294-6172
www.brovennatrading.example
Look and feel

```html
<!DOCTYPE html>
<html lang="en">
<head>
<meta charset="utf-8">
<title>Brovenna Trading and Shipping — Business Card Front</title>
<link rel="stylesheet" href="https://fonts.googleapis.com/css2?family=Cinzel:wght@700&family=Libre+Baskerville:wght@700&display=swap">
<style>
  :root {
    --gold: #dba215;
    --burgundy: #48000b;
    --ink: #0b0705;
  }
  html, body {
    margin: 0;
    padding: 0;
    width: 1200px;
    height: 667px;
    overflow: hidden;
    background: var(--gold);
  }
  .card-front {
    position: relative;
    width: 1200px;
    height: 667px;
    overflow: hidden;
    background: var(--gold);
  }
  .velvet-sweep {
    position: absolute;
    inset: 0;
    width: 1200px;
    height: 667px;
    display: block;
  }
  .brand-lockup {
    position: absolute;
    left: 855px;
    top: 78px;
    transform: translateX(-50%);
    text-align: center;
    color: var(--ink);
    white-space: nowrap;
  }
  .brand-name {
    margin: 0;
    font-family: "Cinzel", "Times New Roman", serif;
    font-weight: 700;
    font-size: 118px;
    line-height: 1;
    letter-spacing: 0;
    transform: scaleX(0.74);
    transform-origin: center;
  }
  .brand-tagline {
    margin: -6px 0 0;
    font-family: "Cinzel", "Times New Roman", serif;
    font-weight: 700;
    font-size: 30px;
    line-height: 1;
    letter-spacing: 0.01em;
  }
  .monogram {
    position: absolute;
    left: 50px;
    top: 329px;
    margin: 0;
    font-family: "Libre Baskerville", "Georgia", serif;
    font-weight: 700;
    font-size: 335px;
    line-height: 1;
    color: var(--gold);
  }
</style>
</head>
<body>
  <main class="card-front">
    <svg class="velvet-sweep" viewBox="0 0 1200 667" aria-hidden="true">
      <path fill="var(--burgundy)"
            d="M0,0 L5,0 C30,150 280,225 610,315 C900,395 1130,470 1165,667 L0,667 Z"/>
    </svg>

    <header class="brand-lockup">
      <h1 class="brand-name">BROVENNA</h1>
      <p class="brand-tagline">Trading and Shipping</p>
    </header>

    <p class="monogram" aria-hidden="true">B</p>
  </main>
</body>
</html>
```